Theme for 60th Anniversary party for a Business

We are looking for a theme for our 60th year party. The theme we used for our 50th party was a movie premier with a drive-in movie. Info on our 50th party is here http://brookwingaero.com/about/50th-anniversary/. The theme must incorporate what we do as a business. Full website at www.brookwingaero.com. The theme would be expanded upon with the use of props or other items to make a large celebration. The party would have around 400 invited guests to take place at our business location on an airport. Please provide details of your theme along with potential props, activities, or other items that would make your theme work. A logo for the theme will also be needed and could be provided with the theme.
Updates

Target Market(s)

Customers, Vendors, Potential Customers

Industry/Entity Type

Movie

Requirements
Must have
• Activities that can take place during event.

```html
<!DOCTYPE html>
<html lang="en">
<head>
<meta charset="utf-8">
<title>Welcome to Brookwing Aero's Speakeasy</title>
<link href="https://fonts.googleapis.com/css2?family=Lobster&family=Monoton&display=swap" rel="stylesheet">
<style>
  :root {
    --ink: #000000;
    --amber: #f39c1f;
  }
  html, body {
    margin: 0;
    padding: 0;
    overflow: hidden;
    background: var(--ink);
  }
  .canvas {
    position: relative;
    width: 1200px;
    height: 1200px;
    background: var(--ink);
    overflow: hidden;
    color: var(--amber);
  }
  .event-title {
    position: absolute;
    top: 72px;
    left: 0;
    width: 1200px;
    margin: 0;
    text-align: center;
    font-family: "Monoton", sans-serif;
    font-weight: 400;
    font-size: 33px;
    letter-spacing: 1px;
    line-height: 48px;
  }
  .theme-grid {
    position: absolute;
    left: 145px;
    top: 207px;
    width: 910px;
    height: 785px;
    box-sizing: border-box;
    border: 4px solid var(--amber);
    display: grid;
    grid-template-columns: repeat(3, 1fr);
    grid-template-rows: repeat(3, 1fr);
  }
  .theme-cell {
    border-right: 4px solid var(--amber);
    border-bottom: 4px solid var(--amber);
    display: flex;
    flex-direction: column;
    align-items: center;
    text-align: center;
    padding-top: 42px;
    box-sizing: border-box;
  }
  .theme-cell:nth-child(3n) { border-right: none; }
  .theme-cell:nth-child(n+7) { border-bottom: none; }
  .theme-cell--centered {
    justify-content: center;
    padding-top: 0;
  }
  .category-heading {
    margin: 0;
    padding-top: 4px;
    font-family: "Monoton", sans-serif;
    font-weight: 400;
    font-size: 52px;
    line-height: 86px;
  }
  .idea {
    margin: 0;
    font-family: "Lobster", cursive;
    font-size: 39px;
    line-height: 58px;
  }
  .idea--under-heading {
    margin-top: -6px;
    line-height: 44px;
  }
</style>
</head>
<body>
<main class="canvas">
  <h1 class="event-title">WELCOME TO BROOKWING AERO'S SPEAKEASY</h1>

  <section class="theme-grid">
    <div class="theme-cell">
      <h2 class="category-heading">ART<br>DECO</h2>
    </div>
    <div class="theme-cell">
      <h2 class="category-heading">CARD<br>GAMES</h2>
    </div>
    <div class="theme-cell">
      <h2 class="category-heading">1920s<br>DRINKS</h2>
      <p class="idea idea--under-heading">moonshine</p>
    </div>

    <div class="theme-cell">
      <p class="idea">draws to<br>win tours or<br>flights</p>
    </div>
    <div class="theme-cell">
      <p class="idea">decks of cards<br>with brookwing<br>aero logo</p>
    </div>
    <div class="theme-cell">
      <p class="idea">live music<br>rat pack</p>
    </div>

    <div class="theme-cell theme-cell--centered">
      <p class="idea">fireworls</p>
    </div>
    <div class="theme-cell">
      <p class="idea">decks of cards<br>with brookwing<br>aero logo</p>
    </div>
    <div class="theme-cell">
      <p class="idea">period<br>dancers</p>
    </div>
  </section>
</main>
</body>
</html>
```